Property Report

8 page document, similar theme to our website (www.harbourandmeadows.com) and previous brochure (provided). All content provided. We want a professional looking document. We need ASAP. Thanks!

Industry/Entity Type

Property

Font styles to use
Serif
Sans Serif

Colors
ffc214
ffcf3e
fee18a
fff3d1

Requirements
Must have
• Page 1: Cover
Page 2: Content
Page 3: About Us
Page 4: Site Description
Page 5: Scheme
Page 6: Analysis
Page 7: Conclusion
Page 8: Contact Details

```html
<!DOCTYPE html>
<html lang="en">
<head>
<meta charset="UTF-8">
<title>Site Description</title>
<link rel="stylesheet" href="https://fonts.googleapis.com/css2?family=Antonio:wght@400&family=Carlito:wght@400;700&display=swap">
<style>
  :root {
    --brand-yellow: #ffc214;
    --title-yellow: #ffc61a;
    --ink: #3f3d4a;
    --white: #ffffff;
    --photo-dark: #5a5a48;
    --photo-brick: #8a6a52;
    --photo-green: #4e5c3c;
  }
  html, body {
    margin: 0;
    padding: 0;
    width: 848px;
    height: 1200px;
    overflow: hidden;
    background: var(--brand-yellow);
  }
  .page {
    position: relative;
    width: 848px;
    height: 1200px;
    background: var(--brand-yellow);
  }
  .hero-photo {
    position: absolute;
    left: 0;
    top: 0;
    width: 848px;
    height: 599px;
    background: linear-gradient(160deg, var(--photo-brick) 0%, #9b8468 40%, #b9b3a2 58%, var(--photo-green) 80%, var(--photo-dark) 100%);
  }
  .page-title {
    position: absolute;
    left: 213px;
    top: 270px;
    margin: 0;
    font-family: "Antonio", "Oswald", sans-serif;
    font-weight: 400;
    font-size: 118px;
    line-height: 135px;
    color: var(--title-yellow);
    letter-spacing: 0;
  }
  .page-title span { display: block; }
  .site-copy {
    position: absolute;
    left: 38px;
    top: 646px;
    width: 410px;
    font-family: "Carlito", "Calibri", sans-serif;
    font-size: 19px;
    line-height: 27.3px;
    color: var(--ink);
  }
  .site-copy p { margin: 0 0 17px; }
  .company-name { font-weight: 700; color: var(--white); }
</style>
</head>
<body>
  <main class="page">
    <div class="hero-photo" role="img" aria-label="Photograph of a terrace of brick houses with white-rendered ground floors, a wall lantern and climbing greenery"></div>
    <h1 class="page-title"><span>Site</span><span>Description</span></h1>
    <section class="site-copy">
      <p><span class="company-name">Harbour and Meadows Commercial</span> have been asked by Daniel Marsh the representative for Marsh Holdings Limited to advise on the best disposal method to maximise value for their property.</p>
      <p>The existing property measures approximately 9,655 square feet internally with parking spaces.</p>
      <p>The site was granted permitted development rights in 2016 to be converted into 11 flats and 11 parking spaces but this was no implemented.</p>
      <p>We understand that the vendors operate their business from the premises and the property has a designated use class of B1(a) Office/E Class.</p>
    </section>
  </main>
</body>
</html>
```